Business card design based on existing website

Please make a business card that is consistent with the look and feel of my new website: http://brindleworth.com.sg. By going to the site, I think you'll have all you need in terms of the work I do and the colors I use.

I would like to ask the winner of this project to then do a separate project to design my stationery.

Target Market(s)

Heads of human resources, people wanting psychotherapy, and executives wanting coaching. (It's quite a mix!)

Industry/Entity Type

Psychology

Contact Information for Business Card

Email: pax5678@brindleworth.com.sg
Website: http://brindleworth.com.sg
Tel: +65 94706152

(I will not have a physical address on the card)

Font styles to use
Serif

Colors

Designer to choose colors to be used in the design.

Requirements
Must have
• On the Front
• ==========
• Have "Dr. Everett Brindleworth" using the font of the website.
• Also "Executive Coach, Psychotherapist, Leadership Professor"
• The back should mention
• ==================
• My degrees
• -------------
• "PhD Kelvale; Post Doc Duncliffe". E.g., "Everett Brindleworth (PhD Kelvale; Post Doc Duncliffe)" where the text between brackets was in smaller font.
• My work
• ----------
• "Executive coach, psychotherapist, and leadership professor"
• My job titles
• ---------------
• "Principal (Brindleworth Consulting)
• Adjunct Professor (Orchid Crest University)
• Adjunct Associate Professor (Meridian Strait University)
• Coach & Supervisor (VORELT) '
• Options:
• 1) you can abbreviate Adjunct Professor to "Adj Prof" or "Adj Professor"; and "Adjunct Associate Professor" to "Adj Assoc Prof"
• 2) you abbreviate "Meridian Strait University" and "Orchid Crest University" to "MSU" and "OCU"
• 3) You can also combine the titles for MSU and OCU, e.g., "Adjunct faculty (MSU & OCU)
Nice to have
• Because I work with many Chinese people, it is sometimes helpful to have my family name, "Brindleworth", in caps. In the past I have not used caps because it takes away from the aesthetic of the card. Only use caps if it looks good.
• The uploaded image of a "EB" is something that may be helpful. I am undecided.
• THANK YOU for helping me!
Should not have
• No photos. In my industry people consider it overselling.

```html
<!DOCTYPE html>
<html lang="en">
<head>
<meta charset="utf-8">
<title>Dr. Everett Brindleworth — Business Card</title>
<link href="https://fonts.googleapis.com/css2?family=EB+Garamond&family=Open+Sans&family=PT+Sans:wght@700&family=PT+Sans+Narrow&display=swap" rel="stylesheet">
<style>
  :root {
    --backdrop: #2b2b2b;
    --card-white: #ffffff;
    --forest: #1b2a1b;
    --body-grey: #474747;
    --cream: #f4f0c8;
  }
  * { margin: 0; padding: 0; box-sizing: border-box; }
  html, body {
    width: 1200px;
    height: 960px;
    overflow: hidden;
    background: var(--backdrop);
  }
  .canvas {
    position: relative;
    width: 1200px;
    height: 960px;
  }
  .card {
    position: absolute;
    width: 600px;
    height: 342px;
  }
  .card-front {
    left: 302px;
    top: 129px;
    background: var(--card-white);
  }
  .card-back {
    left: 299px;
    top: 488px;
    background: var(--forest);
    display: flex;
    align-items: center;
    justify-content: center;
  }
  .identity {
    position: absolute;
    left: 42px;
    top: 36px;
  }
  .name {
    font-family: "PT Sans", sans-serif;
    font-weight: 700;
    font-size: 23px;
    line-height: 28px;
    color: var(--forest);
    letter-spacing: 0.2px;
  }
  .degrees {
    font-family: "PT Sans Narrow", sans-serif;
    font-size: 13.5px;
    line-height: 16px;
    color: var(--forest);
    margin-bottom: 3px;
  }
  .roles {
    font-family: "Open Sans", sans-serif;
    font-size: 12.5px;
    line-height: 16.5px;
    color: var(--body-grey);
  }
  .contact {
    position: absolute;
    right: 41px;
    top: 262px;
    text-align: right;
    font-family: "Open Sans", sans-serif;
    font-size: 12.5px;
    line-height: 16.5px;
    color: var(--body-grey);
  }
  .back-name {
    font-family: "EB Garamond", serif;
    font-size: 47px;
    font-weight: 400;
    color: var(--cream);
    margin-top: 2px;
  }
</style>
</head>
<body>
  <main class="canvas">
    <section class="card card-front">
      <div class="identity">
        <h1 class="name">DR. EVERETT BRINDLEWORTH</h1>
        <p class="degrees">(PhD Kelvale; Post Doc Duncliffe)</p>
        <p class="roles">
          Executive coach, psychotherapist, and<br>
          leadership trainer Principal (Brindleworth Consulting)<br>
          Adj Prof (OCU) Adj Assoc Prof(MSU)<br>
          Coach &amp; Supervisor (VORELT)
        </p>
      </div>
      <address class="contact" style="font-style: normal;">
        +65 94706152<br>
        pax5678@brindleworth.com.sg<br>
        www.brindleworth.com.sg
      </address>
    </section>
    <section class="card card-back">
      <h2 class="back-name">Dr. Everett Brindleworth</h2>
    </section>
  </main>
</body>
</html>
```